KeyHarbor needs a modern business card

We are a modern conveyancing company and we need to appeal to the top (Multi-million dollar properties)and bottom on the property conveyancing market but our sweet spot is the middle of the market. I like professional with a hint of unconventional.

Target Market(s)

As above

Industry/Entity Type

Real Estate

Contact Information for Business Card

Back Of card:
thinking black with the logo and a tag line (I could be wrong about the black)
Tag line - Right Expertise, Exceptional Service

Front of Card:
Marissa Toll (BBus (Finance) LLB)
Licensed Conveyancer
Email: marissa@keyharbor.com.au

Key Harbor
ABN: 48 913 706
Suite 14, Level 3, 9 Calloway Road Lindhurst Park, NSW 2178
Phone: 1300 682 917

Sydney - Melbourne - Brisbane (Perhaps have this along the bottom of the card)

Requirements
Must have
• Sleek, modern and top end appeal (But approachable)
Should not have
• Not too cluttered

```html
<!DOCTYPE html>
<html lang="en">
<head>
<meta charset="utf-8">
<title>KeyHarbor Business Card</title>
<link href="https://fonts.googleapis.com/css2?family=Questrial&family=Montserrat:wght@600&display=swap" rel="stylesheet">
<style>
  :root {
    --bg: #e9ecef;
    --navy: #1f4e79;
    --green: #8cc63f;
    --green-dark: #5aa832;
    --sky-top: #3fc6f2;
    --sky-bottom: #3f8ed6;
    --ink: #444a50;
    --white: #ffffff;
  }
  * { box-sizing: border-box; margin: 0; padding: 0; }
  html, body { width: 1200px; height: 900px; overflow: hidden; }
  body {
    background: var(--bg);
    font-family: "Questrial", sans-serif;
    position: relative;
  }
  .card {
    position: absolute;
    width: 520px;
    height: 318px;
    border-radius: 20px;
    overflow: hidden;
    box-shadow: 0 10px 30px rgba(0,0,0,0.18);
  }

  /* Back of card */
  .card-back {
    left: 70px;
    top: 140px;
    background: linear-gradient(180deg, var(--sky-top), var(--sky-bottom));
  }
  .card-back .brand {
    position: absolute;
    left: 0; right: 0; top: 118px;
    display: flex; align-items: center; justify-content: center; gap: 12px;
  }
  .card-back .brand-mark {
    width: 30px; height: 30px; background: var(--navy);
  }
  .card-back .brand-name {
    font-size: 38px; color: var(--white);
  }
  .card-back .tagline {
    position: absolute;
    right: 34px; bottom: 28px;
    font-size: 14px; letter-spacing: 0.5px;
    color: var(--white); text-transform: uppercase;
  }

  /* Front of card */
  .card-front {
    left: 610px;
    top: 440px;
    background: var(--white);
  }
  .card-front .brand {
    position: absolute;
    left: 290px; top: 56px;
    display: flex; align-items: center; gap: 10px;
  }
  .card-front .brand-mark {
    width: 26px; height: 26px; background: var(--navy);
  }
  .card-front .brand-name {
    font-size: 32px; color: var(--ink);
  }
  .person {
    position: absolute;
    left: 38px; top: 150px;
  }
  .person-name {
    font-family: "Montserrat", sans-serif;
    font-weight: 600;
    font-size: 23px;
    text-transform: uppercase;
    color: var(--navy);
  }
  .person-name .surname { color: var(--green-dark); }
  .person-role {
    font-size: 15px; line-height: 1.3; color: var(--green-dark);
  }
  .contact {
    position: absolute;
    left: 290px; top: 128px;
    list-style: none;
    font-size: 13px; line-height: 1.55; color: var(--ink);
  }
  .contact li { display: flex; align-items: flex-start; gap: 6px; }
  .contact .label { color: var(--green-dark); }
  .contact svg { flex: none; margin-top: 4px; }
  .bands {
    position: absolute; left: 0; bottom: 0;
  }
  .cities {
    position: absolute;
    left: 32px; bottom: 9px;
    font-size: 15px; letter-spacing: 0.6px;
    color: var(--white); text-transform: uppercase;
  }
</style>
</head>
<body>

<section class="card card-back" aria-label="Back of business card">
  <div class="brand">
    <span class="brand-mark"></span>
    <span class="brand-name">KeyHarbor</span>
  </div>
  <p class="tagline">Right Expertise, Exceptional Service</p>
</section>

<section class="card card-front" aria-label="Front of business card">
  <div class="brand">
    <span class="brand-mark"></span>
    <span class="brand-name">KeyHarbor</span>
  </div>

  <div class="person">
    <h1 class="person-name">Marissa <span class="surname">Toll</span></h1>
    <p class="person-role">BBus (Finance) LLB</p>
    <p class="person-role">Licensed Conveyancer</p>
  </div>

  <ul class="contact">
    <li><span><span class="label">ABN:</span> 48 913 706</span></li>
    <li>
      <svg width="9" height="12" viewBox="0 0 9 12" aria-hidden="true"><rect x="1" y="0.5" width="7" height="11" rx="1.5" fill="none" stroke="var(--navy)" stroke-width="1.3"/><circle cx="4.5" cy="9" r="0.9" fill="var(--navy)"/></svg>
      <span>1300 682 917</span>
    </li>
    <li>
      <svg width="11" height="9" viewBox="0 0 11 9" aria-hidden="true"><rect x="0.6" y="0.6" width="9.8" height="7.8" fill="none" stroke="var(--navy)" stroke-width="1.2"/><path d="M0.6 0.8 L5.5 5 L10.4 0.8" fill="none" stroke="var(--navy)" stroke-width="1.2"/></svg>
      <span>marissa@keyharbor.com.au</span>
    </li>
    <li><span>Suite 14, Level 3, 9 Calloway<br>Road Lindhurst Park, NSW 2178</span></li>
  </ul>

  <svg class="bands" width="520" height="60" viewBox="0 0 520 60" aria-hidden="true">
    <polygon points="0,22 350,22 336,60 0,60" fill="var(--navy)"/>
    <polygon points="360,0 520,0 520,60 342,60" fill="var(--green)"/>
  </svg>
  <p class="cities">Sydney - Melbourne - Brisbane</p>
</section>

</body>
</html>
```